Folded A4 flyer for design&construction company

Folded A4 flyer needed. Keywords: elegant, stylish
our website www.dravimo.ae

Industry/Entity Type

Construction

```html
<!DOCTYPE html>
<html lang="en">
<head>
<meta charset="utf-8">
<title>Dravimo – Folded Flyer</title>
<link rel="stylesheet" href="https://fonts.googleapis.com/css2?family=Raleway:wght@400;500;700;800&family=Roboto:wght@500;700&family=Kaushan+Script&family=Dancing+Script:wght@500&display=swap">
<style>
:root{
  --backdrop:#3a3a3c;
  --paper:#ffffff;
  --gold:#b8952f;
  --gold-light:#e6c44e;
  --gold-deep:#9d7c22;
  --ink:#111111;
  --text:#555555;
  --panel:#4a4a4a;
  --bracket:#cfcfcf;
}
*{margin:0;padding:0;box-sizing:border-box}
html,body{width:1200px;height:1200px;overflow:hidden;background:var(--backdrop)}
body{font-family:"Raleway",sans-serif;color:var(--text)}
.canvas{position:relative;width:1200px;height:1200px;background:radial-gradient(ellipse at 50% 40%,#4a4a4c,var(--backdrop) 75%)}
.spread{position:absolute;left:204px;width:740px;height:523px;box-shadow:0 6px 22px rgba(0,0,0,.45);background:var(--paper)}
.spread--outside{top:69px}
.spread--inside{top:602px}
.spread svg{position:absolute;left:0;top:0}
.fold{position:absolute;left:364px;top:0;width:1px;height:523px;background:#222;opacity:.7}
.page{position:absolute;top:0;height:523px}
.page--left{left:0;width:364px}
.page--right{left:364px;width:376px}

.intro{position:absolute;left:32px;top:45px;width:320px;font-size:9.8px;line-height:13.3px;text-align:justify;color:#666}

.quote-box{position:absolute;left:54px;top:299px;width:264px;height:110px;text-align:center;color:#fff;padding-top:30px}
.quote-box .lead{font-size:13px;letter-spacing:.2px;font-weight:400}
.quote-box .lead b{font-weight:800}
.quote-box .phone{font-family:"Roboto",sans-serif;font-weight:700;font-size:25px;line-height:30px;letter-spacing:.5px}
.quote-box .mail{font-family:"Roboto",sans-serif;font-weight:500;font-size:11.5px}

.contact{position:absolute;left:32px;font-size:9.5px;color:#fff;line-height:12px}
.contact .dot{position:absolute;left:0;top:1px;width:12px;height:12px;border-radius:50%;border:1px solid rgba(255,255,255,.6);background:rgba(0,0,0,.12)}
.contact span{display:block;padding-left:21px}
.contact--web{top:443px}
.contact--web b{font-weight:700}
.contact--addr{top:463px}

.brand{position:absolute;text-align:center;color:var(--ink);font-weight:500;letter-spacing:1px;line-height:1}
.brand--cover{left:0;width:376px;top:140px;font-size:50px}
.brand--cover .tag{display:block;margin-top:4px;font-family:"Dancing Script",cursive;font-size:16px;color:var(--gold-deep);letter-spacing:0}
.brand--small{width:140px;font-size:29px}
.brand--small .tag{display:flex;align-items:center;justify-content:center;gap:5px;margin-top:3px;font-size:11px;color:var(--gold-deep);letter-spacing:.4px}
.brand--small .tag::before,.brand--small .tag::after{content:"";flex:1;height:1px;background:var(--gold-deep)}

.motto{position:absolute;left:0;width:376px;top:378px;text-align:center;font-family:"Kaushan Script",cursive;color:var(--ink);font-size:29px;line-height:40px}
.motto .by{display:block;font-family:"Raleway",sans-serif;font-style:italic;font-size:14px;color:#fff;line-height:20px;margin-top:2px}

.services{position:absolute;list-style:none;font-size:9.4px;color:#555;padding:9px 10px 9px 23px}
.services::before,.services::after{content:"";position:absolute;top:0;bottom:0;width:6px;border:3px solid var(--bracket)}
.services::before{left:0;border-right:none}
.services::after{right:0;border-left:none}
.services li{position:relative;white-space:nowrap}
.services li::before{content:"·";position:absolute;left:-11px}
.services li.wrap{line-height:13px;padding-bottom:2px}
.services--design{left:190px;top:32px;width:150px;height:161px;line-height:15.8px}
.services--landscape{left:191px;top:212px;width:149px;height:112px;line-height:16.3px;padding-left:29px}
.services--fitout{left:189px;top:72px;width:150px;height:168px;line-height:15.4px}
.services--maint{left:189px;top:251px;width:150px;height:149px;line-height:16.6px;padding-left:34px}
</style>
</head>
<body>
<div class="canvas">

  <!-- Outside spread: back panel and cover -->
  <section class="spread spread--outside">
    <svg width="740" height="523" viewBox="0 0 740 523">
      <defs>
        <linearGradient id="goldFill" x1="0" y1="0" x2="0" y2="1">
          <stop offset="0" stop-color="#a8862a"/>
          <stop offset="1" stop-color="#c29e34"/>
        </linearGradient>
        <radialGradient id="goldGlow" cx=".6" cy=".85" r=".8">
          <stop offset="0" stop-color="#ecc94f"/>
          <stop offset="1" stop-color="#b08f2d"/>
        </radialGradient>
        <linearGradient id="loungeTone" x1="0" y1="0" x2="1" y2="1">
          <stop offset="0" stop-color="#4a3322"/>
          <stop offset=".5" stop-color="#8a6a4a"/>
          <stop offset="1" stop-color="#c39a6b"/>
        </linearGradient>
        <radialGradient id="roomWarm" cx=".5" cy=".4" r=".7">
          <stop offset="0" stop-color="#f0d08a"/>
          <stop offset="1" stop-color="#b2742e"/>
        </radialGradient>
      </defs>
      <path d="M0,160 C100,132 230,148 364,236 L364,248 C230,166 100,150 0,174 Z" fill="#0d0d0d"/>
      <g role="img" aria-label="Photo of a modern lounge with two white armchairs and a fireplace">
        <path d="M0,174 C100,150 230,166 364,248 L364,300 C240,286 120,302 0,344 Z" fill="url(#loungeTone)"/>
      </g>
      <path d="M0,372 C120,318 240,296 364,306 L364,523 L0,523 Z" fill="url(#goldFill)"/>
      <rect x="54" y="299" width="264" height="110" rx="14" fill="#4a4a4a"/>
      <g transform="translate(364,0)">
        <path d="M0,258 C140,262 300,236 376,208 L376,523 L0,523 Z" fill="url(#goldGlow)"/>
        <path d="M300,232 C335,220 360,205 376,192 L376,208 C350,222 325,230 300,236 Z" fill="#0d0d0d"/>
        <g role="img" aria-label="Photo of a bright hotel lobby interior">
          <circle cx="80" cy="274" r="48" fill="url(#roomWarm)" stroke="#fff" stroke-width="5"/>
        </g>
        <g role="img" aria-label="Photo of a villa hallway with open doors">
          <circle cx="186" cy="274" r="48" fill="#c89a5a" stroke="#fff" stroke-width="5"/>
        </g>
        <g role="img" aria-label="Photo of a classic living room with sofas">
          <circle cx="292" cy="274" r="48" fill="#9a6a3e" stroke="#fff" stroke-width="5"/>
        </g>
      </g>
    </svg>
    <div class="fold"></div>

    <div class="page page--left">
      <p class="intro">We believe in quality beginnings and flawless finishes. We are a team of creative designers and constructors with years of experience and expertise in providing complete interior design and construction services. Our unique designing prowess is complemented by our unflinching commitment to quality construction. Our team specializes in classic and contemporary high quality construction in Dubai for commercial and residential projects.</p>
      <div class="quote-box">
        <div class="lead">GET A <b>FREE QUOTE</b> TODAY!</div>
        <div class="phone">050 4812 337</div>
        <div class="mail">OR CONTACT@DRAVIMO.AE</div>
      </div>
      <div class="contact contact--web"><i class="dot"></i><span>www.<b>dravimo</b>.ae</span></div>
      <div class="contact contact--addr"><i class="dot"></i><span>Dravimo LLC, Harbor Point Tower,<br>Office 806, Business Bay, Dubai</span></div>
    </div>

    <div class="page page--right">
      <div class="brand brand--cover">DRAVIMO<span class="tag">design &amp; construction</span></div>
      <p class="motto">Quality is not an act,<br>it is a habit<span class="by">– Old Proverb</span></p>
    </div>
  </section>

  <!-- Inside spread: services -->
  <section class="spread spread--inside">
    <svg width="740" height="523" viewBox="0 0 740 523">
      <defs>
        <linearGradient id="goldBase" x1="0" y1="0" x2="1" y2="0">
          <stop offset="0" stop-color="#b08f2d"/>
          <stop offset="1" stop-color="#c6a23a"/>
        </linearGradient>
        <linearGradient id="diningTone" x1="0" y1="0" x2="1" y2="0">
          <stop offset="0" stop-color="#3c3340"/>
          <stop offset=".5" stop-color="#d9d6d2"/>
          <stop offset="1" stop-color="#6a5a48"/>
        </linearGradient>
        <linearGradient id="ceilingTone" x1="0" y1="0" x2="1" y2="0">
          <stop offset="0" stop-color="#8a8a90"/>
          <stop offset="1" stop-color="#e8e8ea"/>
        </linearGradient>
      </defs>
      <path d="M0,340 C120,326 250,332 364,398 L364,410 C250,346 120,340 0,354 Z" fill="#0d0d0d"/>
      <g role="img" aria-label="Photo of a luxury dining room with purple chairs">
        <path d="M0,354 C120,340 250,346 364,410 L364,468 C250,462 120,470 0,495 Z" fill="url(#diningTone)"/>
      </g>
      <path d="M0,523 L0,512 C120,478 250,470 364,472 L364,523 Z" fill="url(#goldBase)"/>
      <g transform="translate(364,0)">
        <path d="M75,0 C150,30 270,48 376,40 L376,58 C270,66 150,48 75,0 Z" fill="#0d0d0d"/>
        <g role="img" aria-label="Photo of an office ceiling with recessed lights">
          <path d="M80,0 L376,0 L376,40 C270,48 150,30 80,0 Z" fill="url(#ceilingTone)"/>
        </g>
        <path d="M0,460 C150,452 300,425 376,392 L376,523 L0,523 Z" fill="url(#goldBase)"/>
        <path d="M320,410 C345,400 365,390 376,382 L376,392 C360,402 340,410 320,414 Z" fill="#0d0d0d"/>
        <g role="img" aria-label="Photo of a modern bathroom with warm lighting">
          <circle cx="70" cy="454" r="46" fill="#b88a4e" stroke="#fff" stroke-width="5"/>
        </g>
        <g role="img" aria-label="Photo of a dark tiled bathroom with a bathtub">
          <circle cx="174" cy="454" r="46" fill="#4a3a2c" stroke="#fff" stroke-width="5"/>
        </g>
        <g role="img" aria-label="Photo of a bedroom with a patterned feature wall">
          <circle cx="282" cy="454" r="46" fill="#3c4a4c" stroke="#fff" stroke-width="5"/>
        </g>
      </g>
    </svg>
    <div class="fold"></div>

    <div class="page page--left">
      <div class="brand brand--small" style="left:32px;top:80px">DRAVIMO<span class="tag">DESIGN</span></div>
      <ul class="services services--design">
        <li>Villas Interior Design</li>
        <li>Villas Exterior Design</li>
        <li>Landscape Design</li>
        <li>Retail Interior Design</li>
        <li>Office Interior Design</li>
        <li>Hospitality Interior Design</li>
        <li>Hotel Interior Design</li>
        <li>Hotel Exterior Design</li>
        <li>Restaurant Interior Design</li>
      </ul>
      <div class="brand brand--small" style="left:32px;top:256px">DRAVIMO<span class="tag">LANDSCAPING</span></div>
      <ul class="services services--landscape">
        <li>Soft Landscaping</li>
        <li>Irrigation Solutions</li>
        <li>Hard land Scaping</li>
        <li>External Lighting</li>
        <li class="wrap">Swimming Pool &amp;<br>Water Features</li>
      </ul>
    </div>

    <div class="page page--right">
      <div class="brand brand--small" style="left:26px;top:140px">DRAVIMO<span class="tag">FITOUT</span></div>
      <ul class="services services--fitout">
        <li>Development Approvals</li>
        <li>Flooring Solutions</li>
        <li>Partition</li>
        <li>Sealing Solutions</li>
        <li>MEP Works</li>
        <li>Civil Works</li>
        <li>Flooring works</li>
        <li>Joinery</li>
        <li class="wrap">Glass and Aluminium<br>Works (subcontractor)</li>
      </ul>
      <div class="brand brand--small" style="left:26px;top:313px">DRAVIMO<span class="tag">MAINTAINCE</span></div>
      <ul class="services services--maint">
        <li>AC Repair</li>
        <li>Plumber Services</li>
        <li>Electric Repair</li>
        <li>Carpentry Work</li>
        <li>Gypsum Ceiling</li>
        <li>Painting Services</li>
        <li>Cleaning Services</li>
        <li>Emergency Services</li>
      </ul>
    </div>
  </section>

</div>
</body>
</html>
```